Harborline Motors LLC

Car Dealer Customer Service
Address: 2741 Linden Avenue, Shelbyville, TN 37162
web: www.harborlinemotorstn.net
email: harborlinemotorstn@mailbox-example.net
Phone: (931) 555-0148
Phone: (629) 555-0173

```html
<!DOCTYPE html>
<html lang="en">
<head>
<meta charset="utf-8">
<title>Harborline Motors – Business Card</title>
<link rel="stylesheet" href="https://fonts.googleapis.com/css2?family=Montserrat:wght@700&family=Arimo:wght@400&family=Exo+2:wght@700&display=swap">
<style>
  :root {
    --backdrop: #262626;
    --card-white: #ffffff;
    --brand-blue: #1c76a6;
    --brand-gold: #ebb146;
    --gold-soft: #f0c060;
    --text-white: #ffffff;
  }
  * { box-sizing: border-box; margin: 0; padding: 0; }
  html, body { width: 1075px; height: 1200px; overflow: hidden; background: var(--backdrop); }
  .canvas { position: relative; width: 1075px; height: 1200px; }

  .card {
    position: absolute;
    width: 664px; height: 396px;
    background: var(--card-white);
    overflow: hidden;
    box-shadow: 3px 3px 4px rgba(0,0,0,.7);
  }
  .card--front { left: 206px; top: 187px; }
  .card--back  { left: 203px; top: 638px; }

  /* front */
  .front-band {
    position: absolute; left: 0; right: 0; top: 226px; bottom: 0;
    background: var(--brand-blue);
  }
  .car-illustration {
    position: absolute; left: 22px; top: 26px; width: 620px; height: 196px;
    background: linear-gradient(180deg, var(--gold-soft), var(--brand-gold));
    border-radius: 110px 110px 30px 30px;
  }
  .person { position: absolute; left: 0; right: 0; top: 250px; text-align: center; color: var(--text-white); }
  .person__name { font: 700 23px/1.1 "Montserrat", sans-serif; }
  .person__title { font: 400 17px/1.2 "Arimo", sans-serif; }

  .contact { position: absolute; top: 304px; left: 0; right: 0; color: var(--text-white); font: 400 16px/24px "Arimo", sans-serif; }
  .contact__address { position: absolute; right: 374px; text-align: right; white-space: nowrap; }
  .contact__divider { position: absolute; left: 300px; top: 4px; width: 1px; height: 64px; background: var(--text-white); }
  .contact__reach { position: absolute; left: 310px; white-space: nowrap; }
  .contact__reach li { list-style: none; display: flex; align-items: center; gap: 5px; }
  .contact__reach svg { width: 15px; height: 15px; fill: var(--text-white); flex: none; }

  /* back */
  .brand-mark {
    position: absolute; left: 242px; top: 57px; width: 180px; height: 180px;
    border-radius: 50%; background: var(--brand-blue);
  }
  .brand-name {
    position: absolute; left: 0; right: 0; top: 246px; text-align: center;
    font: 700 44px/1 "Exo 2", sans-serif; color: var(--brand-blue); letter-spacing: 1px;
  }
  .tagline-band {
    position: absolute; left: 0; right: 0; top: 310px; height: 51px;
    background: var(--brand-blue);
    border-top: 3px solid var(--brand-gold);
    border-bottom: 3px solid var(--brand-gold);
    display: flex; align-items: center; justify-content: center;
  }
  .tagline { font: 700 24px/1 "Exo 2", sans-serif; color: var(--text-white); letter-spacing: 2.5px; text-transform: uppercase; }
</style>
</head>
<body>
<main class="canvas">
  <section class="card card--front">
    <div class="front-band"></div>
    <div class="car-illustration" role="img" aria-label="Illustration of a vintage yellow roadster car in side view"></div>
    <div class="person">
      <p class="person__name">MARCUS BELLAMY</p>
      <p class="person__title">Managing Director</p>
    </div>
    <div class="contact">
      <div class="contact__address">
        <p>2741 Linden Avenue</p>
        <p>Shelbyville, TN 37162</p>
        <p>www.harborlinemotorstn.net</p>
      </div>
      <div class="contact__divider"></div>
      <ul class="contact__reach">
        <li><svg viewBox="0 0 24 24"><path d="M6.6 10.8a15.1 15.1 0 0 0 6.6 6.6l2.2-2.2a1 1 0 0 1 1-.25 11.4 11.4 0 0 0 3.6.6 1 1 0 0 1 1 1V20a1 1 0 0 1-1 1A17 17 0 0 1 3 4a1 1 0 0 1 1-1h3.5a1 1 0 0 1 1 1c0 1.25.2 2.45.6 3.6a1 1 0 0 1-.25 1z"/></svg>(931) 555-0148</li>
        <li><svg viewBox="0 0 24 24"><path d="M6.6 10.8a15.1 15.1 0 0 0 6.6 6.6l2.2-2.2a1 1 0 0 1 1-.25 11.4 11.4 0 0 0 3.6.6 1 1 0 0 1 1 1V20a1 1 0 0 1-1 1A17 17 0 0 1 3 4a1 1 0 0 1 1-1h3.5a1 1 0 0 1 1 1c0 1.25.2 2.45.6 3.6a1 1 0 0 1-.25 1z"/></svg>(629) 555-0173</li>
        <li><svg viewBox="0 0 24 24"><path d="M2 5h20v14H2zm2 2v.5l8 5 8-5V7zm0 2.8V17h16V9.8l-8 5z"/></svg>harborlinemotorstn@mailbox-example.net</li>
      </ul>
    </div>
  </section>

  <section class="card card--back">
    <div class="brand-mark"></div>
    <p class="brand-name">HARBORLINE MOTORS</p>
    <div class="tagline-band"><p class="tagline">Car Dealer Customer Service</p></div>
  </section>
</main>
</body>
</html>
```